ESCORT DIRECTORY

This website is an advertising and information resource , we only sell advertisement space.
The requirement:
-- 7 Banners with different size
--sexy girl on the banner
-- the sexy girl will have different position on each banner
--I want my logo on the banner (Upload files)
-- I want the word : " ADVERTISE FOR FREE" in a beautiful presentation

```html
<!DOCTYPE html>
<html lang="en">
<head>
<meta charset="utf-8">
<title>Directory Banner Set</title>
<link href="https://fonts.googleapis.com/css2?family=Roboto:wght@300;400;500&display=swap" rel="stylesheet">
<style>
:root{
  --page:#ffffff;
  --ink:#111111;
  --panel-light:#fdeef6;
  --panel-mid:#f8c4df;
  --panel-soft:#fbd9eb;
  --accent:#ec3d9a;
  --accent-deep:#d81b7d;
  --accent-text:#d0186f;
  --button:#050505;
  --button-text:#ffffff;
  --photo-hot:#e7298a;
  --photo-pink:#f39ccc;
  --photo-blush:#f7c6e0;
  --photo-skin:#e9a7a0;
  --photo-dark:#3a2630;
  --photo-grey:#7a6f76;
}
*{margin:0;padding:0;box-sizing:border-box}
html,body{width:1200px;height:864px;overflow:hidden;background:var(--page)}
body{position:relative;font-family:"Roboto",Arial,sans-serif;color:var(--ink)}
.size-label{position:absolute;font-size:16px;font-weight:400;letter-spacing:.2px}
.banner{position:absolute;overflow:hidden;background:linear-gradient(160deg,var(--panel-light) 0%,var(--panel-soft) 55%,var(--panel-mid) 100%)}
.banner svg.art{position:absolute;inset:0;width:100%;height:100%}
.content{position:absolute;display:flex;flex-direction:column;align-items:center;justify-content:center;text-align:center}
.brand{display:flex;flex-direction:column;align-items:center}
.brand-mark{background:var(--accent)}
.brand-name{font-weight:300;color:var(--ink);letter-spacing:.3em;white-space:nowrap;margin-right:-.3em}
.cta{background:var(--button);color:var(--button-text);font-weight:500;border-radius:999px;line-height:1.3;white-space:nowrap}
.promo{color:var(--accent-text);font-weight:400;line-height:1.4;white-space:nowrap}
</style>
</head>
<body>
<svg width="0" height="0" style="position:absolute">
  <defs>
    <linearGradient id="band" x1="0" y1="0" x2="1" y2="1"><stop offset="0" stop-color="#f7a6d0"/><stop offset=".5" stop-color="var(--accent)"/><stop offset="1" stop-color="var(--accent-deep)"/></linearGradient>
    <linearGradient id="bandH" x1="0" y1="0" x2="1" y2="0"><stop offset="0" stop-color="var(--accent-deep)"/><stop offset=".5" stop-color="var(--accent)"/><stop offset="1" stop-color="#f7a6d0"/></linearGradient>
    <radialGradient id="glow" cx=".5" cy=".45" r=".55"><stop offset="0" stop-color="var(--photo-skin)" stop-opacity=".85"/><stop offset="1" stop-color="var(--photo-skin)" stop-opacity="0"/></radialGradient>
    <radialGradient id="hotspot" cx=".5" cy=".5" r=".5"><stop offset="0" stop-color="var(--photo-hot)" stop-opacity=".9"/><stop offset="1" stop-color="var(--photo-hot)" stop-opacity="0"/></radialGradient>
  </defs>
</svg>

<!-- 500 x 350 -->
<div class="size-label" style="left:67px;top:62px">500 * 350</div>
<div class="banner" style="left:67px;top:92px;width:337px;height:236px">
  <svg class="art" viewBox="0 0 337 236" preserveAspectRatio="none">
    <defs><linearGradient id="ph1" x1="0" y1="0" x2="1" y2="1"><stop offset="0" stop-color="var(--photo-grey)"/><stop offset=".45" stop-color="var(--photo-blush)"/><stop offset="1" stop-color="var(--photo-hot)"/></linearGradient></defs>
    <path d="M0 236 Q40 120 0 30 Z" fill="#fff" opacity=".35"/>
    <path d="M150 0 Q250 118 160 236 L214 236 Q290 118 212 0 Z" fill="#fff" opacity=".3"/>
    <g role="img" aria-label="Photo of a model in pink lingerie">
      <path d="M212 0 Q290 118 214 236 L337 236 L337 0 Z" fill="url(#ph1)"/>
      <ellipse cx="290" cy="110" rx="55" ry="95" fill="url(#glow)"/>
      <ellipse cx="290" cy="200" rx="50" ry="30" fill="url(#hotspot)"/>
    </g>
    <path d="M204 0 Q284 118 208 236 L222 236 Q298 118 220 0 Z" fill="url(#band)"/>
  </svg>
  <div class="content" style="left:0;top:0;width:222px;height:236px">
    <div class="brand"><div class="brand-mark" style="width:30px;height:30px;margin-bottom:9px"></div><div class="brand-name" style="font-size:16px">VELVETLINE</div></div>
    <div class="cta" style="font-size:12.5px;padding:9px 9px;border-radius:16px;margin-top:15px">ESCORT<br>DIRECTORY<br>➜</div>
    <div class="promo" style="font-size:8.5px;margin-top:17px">ADVERTISE FOR FREE</div>
  </div>
</div>

<!-- 725 x 210 -->
<div class="size-label" style="left:472px;top:62px">725 * 210</div>
<div class="banner" style="left:472px;top:92px;width:491px;height:142px">
  <svg class="art" viewBox="0 0 491 142" preserveAspectRatio="none">
    <defs><linearGradient id="ph2" x1="0" y1="0" x2="1" y2="1"><stop offset="0" stop-color="var(--photo-dark)"/><stop offset=".35" stop-color="var(--photo-skin)"/><stop offset=".6" stop-color="var(--photo-hot)"/><stop offset="1" stop-color="var(--photo-grey)"/></linearGradient></defs>
    <path d="M0 142 Q30 70 0 10 Z" fill="#fff" opacity=".35"/>
    <g role="img" aria-label="Photo of a reclining model with a pink scarf">
      <path d="M160 0 Q250 71 176 142 L491 142 L491 0 Z" fill="url(#ph2)"/>
      <ellipse cx="320" cy="80" rx="80" ry="55" fill="url(#hotspot)"/>
      <ellipse cx="420" cy="60" rx="70" ry="40" fill="url(#glow)"/>
    </g>
    <path d="M152 0 Q242 71 168 142 L180 142 Q256 71 166 0 Z" fill="url(#band)"/>
  </svg>
  <div class="content" style="left:0;top:0;width:196px;height:142px">
    <div class="brand"><div class="brand-mark" style="width:24px;height:24px;margin-bottom:7px"></div><div class="brand-name" style="font-size:13px">VELVETLINE</div></div>
    <div class="cta" style="font-size:10px;padding:9px 12px;margin-top:11px">ESCORT DIRECTORY ➜</div>
    <div class="promo" style="font-size:7px;margin-top:8px">ADVERTISE FOR FREE</div>
  </div>
</div>

<!-- 160 x 600 -->
<div class="size-label" style="left:1030px;top:62px">160 * 600</div>
<div class="banner" style="left:1030px;top:92px;width:108px;height:404px">
  <svg class="art" viewBox="0 0 108 404" preserveAspectRatio="none">
    <defs><linearGradient id="ph3" x1="0" y1="0" x2="0" y2="1"><stop offset="0" stop-color="var(--photo-dark)"/><stop offset=".4" stop-color="var(--photo-skin)"/><stop offset=".7" stop-color="var(--photo-dark)"/><stop offset="1" stop-color="var(--photo-grey)"/></linearGradient></defs>
    <g role="img" aria-label="Photo of a model in black lingerie">
      <path d="M0 0 H108 V222 Q54 204 0 218 Z" fill="url(#ph3)"/>
      <ellipse cx="25" cy="60" rx="30" ry="40" fill="url(#hotspot)"/>
      <ellipse cx="90" cy="150" rx="25" ry="40" fill="url(#hotspot)"/>
    </g>
    <path d="M0 214 Q54 200 108 218 V232 Q54 212 0 226 Z" fill="url(#bandH)"/>
  </svg>
  <div class="content" style="left:0;top:228px;width:108px;height:176px">
    <div class="brand"><div class="brand-mark" style="width:20px;height:20px;margin-bottom:6px"></div><div class="brand-name" style="font-size:10.5px;letter-spacing:.2em;margin-right:-.2em">VELVETLINE</div></div>
    <div class="cta" style="font-size:11.5px;padding:8px 8px;border-radius:14px;margin-top:12px">ESCORT<br>DIRECTORY<br>➜</div>
    <div class="promo" style="font-size:8.5px;margin-top:9px">ADVERTISE<br>FOR FREE</div>
  </div>
</div>

<!-- 720 x 300 -->
<div class="size-label" style="left:472px;top:271px">720 * 300</div>
<div class="banner" style="left:472px;top:301px;width:485px;height:202px">
  <svg class="art" viewBox="0 0 485 202" preserveAspectRatio="none">
    <defs><linearGradient id="ph4" x1="0" y1="0" x2="1" y2="1"><stop offset="0" stop-color="var(--photo-blush)"/><stop offset=".5" stop-color="var(--photo-pink)"/><stop offset="1" stop-color="var(--photo-blush)"/></linearGradient></defs>
    <path d="M0 202 Q40 100 0 20 Z" fill="#fff" opacity=".35"/>
    <g role="img" aria-label="Photo of a model lying on pink bed sheets">
      <path d="M168 0 Q250 101 174 202 L485 202 L485 0 Z" fill="url(#ph4)"/>
      <ellipse cx="340" cy="70" rx="90" ry="45" fill="url(#hotspot)"/>
      <ellipse cx="280" cy="130" rx="70" ry="40" fill="url(#glow)"/>
    </g>
    <path d="M160 0 Q242 101 166 202 L180 202 Q258 101 176 0 Z" fill="url(#band)"/>
  </svg>
  <div class="content" style="left:0;top:0;width:196px;height:202px">
    <div class="brand"><div class="brand-mark" style="width:32px;height:32px;margin-bottom:10px"></div><div class="brand-name" style="font-size:17px">VELVETLINE</div></div>
    <div class="cta" style="font-size:11.5px;padding:10px 12px;margin-top:18px">ESCORT DIRECTORY ➜</div>
    <div class="promo" style="font-size:8.5px;margin-top:14px">ADVERTISE FOR FREE</div>
  </div>
</div>

<!-- 120 x 600 -->
<div class="size-label" style="left:67px;top:366px">120 * 600</div>
<div class="banner" style="left:67px;top:396px;width:81px;height:404px">
  <svg class="art" viewBox="0 0 81 404" preserveAspectRatio="none">
    <defs><linearGradient id="ph5" x1="0" y1="0" x2="0" y2="1"><stop offset="0" stop-color="var(--photo-pink)"/><stop offset=".35" stop-color="var(--photo-skin)"/><stop offset=".6" stop-color="var(--photo-dark)"/><stop offset="1" stop-color="var(--photo-pink)"/></linearGradient></defs>
    <g role="img" aria-label="Photo of a standing model in lingerie">
      <path d="M0 0 H81 V222 Q40 206 0 220 Z" fill="url(#ph5)"/>
      <ellipse cx="8" cy="80" rx="18" ry="60" fill="url(#hotspot)"/>
    </g>
    <path d="M0 216 Q40 202 81 218 V232 Q40 214 0 228 Z" fill="url(#bandH)"/>
  </svg>
  <div class="content" style="left:0;top:228px;width:81px;height:176px">
    <div class="brand"><div class="brand-mark" style="width:17px;height:17px;margin-bottom:5px"></div><div class="brand-name" style="font-size:8px;letter-spacing:.16em;margin-right:-.16em">VELVETLINE</div></div>
    <div class="cta" style="font-size:9.5px;padding:7px 9px;border-radius:13px;margin-top:14px">ESCORT<br>DIRECTORY<br>➜</div>
    <div class="promo" style="font-size:7.5px;margin-top:9px">ADVERTISE<br>FOR FREE</div>
  </div>
</div>

<!-- 300 x 600 -->
<div class="size-label" style="left:202px;top:366px">300 * 600</div>
<div class="banner" style="left:202px;top:396px;width:202px;height:404px">
  <svg class="art" viewBox="0 0 202 404" preserveAspectRatio="none">
    <defs><linearGradient id="ph6" x1="0" y1="0" x2="1" y2="0"><stop offset="0" stop-color="var(--photo-hot)"/><stop offset=".3" stop-color="var(--photo-grey)"/><stop offset=".55" stop-color="var(--photo-dark)"/><stop offset=".8" stop-color="var(--photo-grey)"/><stop offset="1" stop-color="var(--photo-hot)"/></linearGradient></defs>
    <path d="M0 404 Q50 320 0 260 Z" fill="#fff" opacity=".35"/>
    <g role="img" aria-label="Photo of a model by a mirror">
      <path d="M0 0 H202 V240 Q120 200 0 232 Z" fill="url(#ph6)"/>
      <ellipse cx="100" cy="40" rx="110" ry="40" fill="url(#hotspot)"/>
    </g>
    <path d="M0 226 Q110 190 202 234 V250 Q120 208 0 242 Z" fill="url(#bandH)"/>
  </svg>
  <div class="content" style="left:0;top:242px;width:202px;height:162px">
    <div class="brand"><div class="brand-mark" style="width:30px;height:30px;margin-bottom:9px"></div><div class="brand-name" style="font-size:16px">VELVETLINE</div></div>
    <div class="cta" style="font-size:11px;padding:10px 18px;margin-top:16px">ESCORT DIRECTORY ➜</div>
    <div class="promo" style="font-size:8.5px;margin-top:10px">ADVERTISE FOR FREE</div>
  </div>
</div>

<!-- 728 x 90 -->
<div class="size-label" style="left:472px;top:541px">728 * 90</div>
<div class="banner" style="left:472px;top:571px;width:491px;height:61px">
  <svg class="art" viewBox="0 0 491 61" preserveAspectRatio="none">
    <defs><linearGradient id="ph7" x1="0" y1="0" x2="1" y2="0"><stop offset="0" stop-color="var(--photo-pink)"/><stop offset=".35" stop-color="var(--photo-skin)"/><stop offset=".6" stop-color="var(--photo-pink)"/><stop offset=".8" stop-color="var(--photo-dark)"/><stop offset="1" stop-color="var(--photo-skin)"/></linearGradient></defs>
    <g role="img" aria-label="Photo of a model resting on a pillow">
      <path d="M230 0 Q252 30 232 61 L491 61 L491 0 Z" fill="url(#ph7)"/>
      <ellipse cx="300" cy="10" rx="60" ry="20" fill="url(#hotspot)"/>
    </g>
    <path d="M224 0 Q246 30 226 61 L236 61 Q258 30 236 0 Z" fill="url(#band)"/>
  </svg>
  <div class="content" style="left:4px;top:0;width:84px;height:61px">
    <div class="brand"><div class="brand-mark" style="width:18px;height:18px;margin-bottom:5px"></div><div class="brand-name" style="font-size:10px;letter-spacing:.18em;margin-right:-.18em">VELVETLINE</div></div>
  </div>
  <div class="content" style="left:92px;top:0;width:130px;height:61px">
    <div class="cta" style="font-size:9px;padding:7px 9px">ESCORT DIRECTORY ➜</div>
    <div class="promo" style="font-size:7px;margin-top:5px">ADVERTISE FOR FREE</div>
  </div>
</div>

</body>
</html>
```